Manufacturing company needs new business card.

I need a unique Business Card that will truly stand out. Nothing too busy. Simple is good, right? Not looking for a standard design either. No cookie cutter layout. I am just looking for something interesting and a bit different. Does't have to completely off the wall crazy, just not your run of the mill business card. Clean and modern with a touch of industrial.

Target Market(s)

Air conditioning industry, Architects, builders.

Industry/Entity Type

Business

Contact Information for Business Card

Details to be included on card are:

Peter Vance
Managing Director

T: 1300 847 519
M: 0428 593 174
W: www.brenvaleworks.com.au
E: peter.vance@brenvaleworks.com.au
A: 58 Harwick Lane, Sydney NSW 2000

Font styles to use
Sans Serif

Colors
0355a3
848484
fbfbfb

Requirements
Must have
• Card design must be landscape.

```html
<!DOCTYPE html>
<html lang="en">
<head>
<meta charset="utf-8">
<title>Brenvale Works Business Card</title>
<link rel="stylesheet" href="https://fonts.googleapis.com/css2?family=Arimo:wght@400&display=swap">
<style>
  :root {
    --card-blue: #1d4fa6;
    --pattern-blue: #2a5cb4;
    --pattern-grey: #848484;
    --ink-white: #fbfbfb;
    --page-bg: #2b2b2b;
  }
  * { margin: 0; padding: 0; box-sizing: border-box; }
  html, body {
    width: 1200px; height: 900px; overflow: hidden;
    background: var(--page-bg);
    font-family: "Arimo", Arial, sans-serif;
    color: var(--ink-white);
  }
  .canvas {
    position: relative; width: 1200px; height: 900px;
  }
  .card {
    position: absolute; left: 290px;
    width: 620px; height: 380px;
    border-radius: 22px;
    background: var(--card-blue);
    overflow: hidden;
  }
  .card--front { top: 50px; }
  .card--back { top: 470px; }

  /* front */
  .front-texture {
    position: absolute; inset: 0;
    background: linear-gradient(135deg, var(--pattern-blue) 0%, var(--card-blue) 55%, #22529f 100%);
  }
  .brand-square {
    position: absolute;
    background: var(--ink-white);
  }
  .card--front .brand-square { left: 44px; bottom: 52px; width: 58px; height: 58px; }

  .wordmark { position: absolute; }
  .wordmark__name {
    font-size: 32px; font-weight: 400; letter-spacing: -0.3px; line-height: 1;
    color: var(--ink-white); white-space: nowrap;
  }
  .wordmark__tag {
    display: flex; align-items: center; gap: 10px; margin-top: 4px;
  }
  .wordmark__rule { flex: 1; height: 2px; background: var(--ink-white); }
  .wordmark__country {
    font-size: 13px; letter-spacing: 8px; line-height: 1; color: var(--ink-white);
  }
  .card--front .wordmark { right: 44px; top: 168px; width: 270px; }

  /* back */
  .card--back .brand-square { left: 40px; top: 112px; width: 56px; height: 56px; }
  .card--back .wordmark { left: 112px; top: 62px; width: 272px; }

  .frame-rule { position: absolute; background: var(--ink-white); }
  .frame-rule--vertical { left: 16px; top: 18px; width: 3px; height: 236px; }
  .frame-rule--horizontal { left: 16px; top: 251px; width: 450px; height: 3px; }

  .person { position: absolute; right: 152px; top: 186px; text-align: right; }
  .person__name { font-size: 22px; letter-spacing: 0.5px; line-height: 1.1; }
  .person__title { font-size: 14px; line-height: 1.3; }

  .address {
    position: absolute; right: 30px; top: 270px;
    text-align: right; font-size: 13px; line-height: 1.35;
  }

  .contact-list {
    position: absolute; left: 36px; top: 270px; list-style: none;
    font-size: 15px; line-height: 1;
  }
  .contact-list li { display: flex; align-items: center; gap: 10px; height: 22px; }
  .contact-list svg { width: 13px; height: 13px; flex: none; }
</style>
</head>
<body>
<main class="canvas">

  <section class="card card--front" aria-label="Business card front">
    <div class="front-texture" role="img" aria-label="Faint repeating pattern of outlined squares in lighter blue and grey"></div>
    <div class="brand-square" aria-hidden="true"></div>
    <div class="wordmark">
      <div class="wordmark__name">Brenvale Works</div>
      <div class="wordmark__tag"><span class="wordmark__rule"></span><span class="wordmark__country">AUSTRALIA</span></div>
    </div>
  </section>

  <section class="card card--back" aria-label="Business card back">
    <div class="frame-rule frame-rule--vertical"></div>
    <div class="frame-rule frame-rule--horizontal"></div>

    <div class="brand-square" aria-hidden="true"></div>
    <div class="wordmark">
      <div class="wordmark__name">Brenvale Works</div>
      <div class="wordmark__tag"><span class="wordmark__rule"></span><span class="wordmark__country">AUSTRALIA</span></div>
    </div>

    <div class="person">
      <div class="person__name">PETER VANCE</div>
      <div class="person__title">Managing Director</div>
    </div>

    <address class="address" style="font-style:normal">58 Harwick Lane<br>Sydney NSW 2000</address>

    <ul class="contact-list">
      <li>
        <svg viewBox="0 0 16 16" aria-hidden="true"><path fill="#fbfbfb" d="M3.6 1.2l2.3 2.6-1.3 1.6c.9 2.1 2.5 3.8 4.6 4.8l1.6-1.3 2.6 2.3-1.2 2.3C7.2 13.6 2.4 8.8 1.5 3.3z"/></svg>
        <span>1300 847 519</span>
      </li>
      <li>
        <svg viewBox="0 0 16 16" aria-hidden="true"><rect x="4" y="1" width="8" height="14" rx="1.5" fill="none" stroke="#fbfbfb" stroke-width="1.6"/><circle cx="8" cy="12.3" r="0.9" fill="#fbfbfb"/></svg>
        <span>0428 593 174</span>
      </li>
      <li>
        <svg viewBox="0 0 16 16" aria-hidden="true"><rect x="1.5" y="3.5" width="13" height="9" fill="none" stroke="#fbfbfb" stroke-width="1.5"/><path d="M1.5 3.5L8 9l6.5-5.5" fill="none" stroke="#fbfbfb" stroke-width="1.5"/></svg>
        <span>peter.vance@brenvaleworks.com.au</span>
      </li>
      <li>
        <svg viewBox="0 0 16 16" aria-hidden="true"><circle cx="8" cy="8" r="6.5" fill="none" stroke="#fbfbfb" stroke-width="1.4"/><ellipse cx="8" cy="8" rx="2.8" ry="6.5" fill="none" stroke="#fbfbfb" stroke-width="1.2"/><path d="M1.5 8h13M2.6 4.7h10.8M2.6 11.3h10.8" stroke="#fbfbfb" stroke-width="1.1"/></svg>
        <span>www.brenvaleworks.com.au</span>
      </li>
    </ul>
  </section>

</main>
</body>
</html>
```